Webpage

I am a professional genealogist. I need a webpage that is professional looking (using the logo I chose), I can add hyperlinks and photos to if and when I want.

```html
<!DOCTYPE html>
<html lang="en">
<head>
<meta charset="utf-8">
<title>Ellison Research Services</title>
<link rel="stylesheet" href="https://fonts.googleapis.com/css2?family=Open+Sans:ital,wght@0,300;0,400;0,600;0,700;1,300;1,400&display=swap">
<style>
  :root {
    --green: #80c0a0;
    --green-text: #6bbd97;
    --teal: #2597a0;
    --teal-bright: #3fb7c6;
    --hero-dark: #0f8896;
    --hero-light: #35b8c8;
    --ink: #333a44;
    --body: #555b63;
    --footer: #4b5264;
    --footer-line: #5f6678;
    --footer-text: #e6e8ee;
    --bottom: #3a404d;
    --white: #ffffff;
  }
  * { box-sizing: border-box; margin: 0; padding: 0; }
  html, body { width: 1061px; height: 1200px; overflow: hidden; }
  body { font-family: "Open Sans", Arial, sans-serif; background: var(--white); color: var(--body); position: relative; }
  .container { width: 738px; margin: 0 auto; position: relative; }

  .topbar { height: 21px; background: var(--green); color: var(--white); font-size: 12px; line-height: 21px; }
  .topbar .container { display: flex; justify-content: space-between; }

  .header { height: 73px; background: var(--white); }
  .header .container { display: flex; justify-content: space-between; align-items: center; height: 73px; }
  .brand { display: flex; align-items: center; gap: 12px; margin-left: 6px; }
  .brand-dot { width: 46px; height: 46px; border-radius: 50%; background: var(--green); }
  .brand-name { font-size: 21px; font-weight: 400; color: var(--ink); letter-spacing: -0.3px; }
  .nav { display: flex; gap: 17px; font-size: 12.5px; color: #666; }
  .nav .active { color: var(--ink); font-weight: 600; }

  .hero { position: relative; height: 431px; overflow: hidden;
    background: radial-gradient(circle at 75% 30%, var(--hero-light), var(--hero-dark) 70%); }
  .hero-photo { position: absolute; left: 519px; top: 0; width: 400px; height: 431px;
    background: linear-gradient(180deg, #9a9a9a, #5e5e5e); }
  .hero-text { position: absolute; left: 162px; top: 194px; width: 410px; color: var(--white);
    text-shadow: 0 1px 2px rgba(0,0,0,0.35); }
  .hero-title { font-size: 31px; font-weight: 600; line-height: 1.15; }
  .hero-sub { font-size: 20px; font-weight: 600; margin-bottom: 10px; }
  .hero-copy { font-size: 15px; font-weight: 700; line-height: 19px; }
  .btn { position: absolute; left: 162px; top: 384px; width: 151px; height: 44px;
    background: linear-gradient(#ffffff, #e4e4e4); border-radius: 3px; color: var(--teal);
    font-size: 20px; font-weight: 600; text-align: center; line-height: 44px;
    box-shadow: 0 2px 4px rgba(0,0,0,0.3); }
  .dots { position: absolute; left: 162px; top: 483px; display: flex; gap: 4px; }
  .dots span { width: 12px; height: 12px; border-radius: 50%; border: 2px solid var(--white); opacity: .6; }
  .dots span.on { opacity: 1; }

  .welcome { text-align: center; padding-top: 30px; }
  .welcome h1 { font-size: 25px; font-weight: 400; color: var(--green-text); }
  .welcome p { width: 650px; margin: 4px auto 0; font-size: 14px; line-height: 19px; font-weight: 300; color: #444; }
  .services h2 { font-size: 20px; font-weight: 400; color: var(--teal); margin-top: 34px; }
  .service-list { display: flex; justify-content: center; gap: 5px; list-style: none; margin-top: 8px;
    font-size: 15px; font-style: italic; color: #444; }
  .service-list li::before { content: ""; display: inline-block; width: 7px; height: 7px; border: 2px solid var(--green);
    border-radius: 50%; margin-right: 3px; vertical-align: 1px; }

  .footer { position: absolute; top: 790px; left: 0; width: 1061px; height: 328px; background: var(--footer); color: var(--footer-text); }
  .footer .container { display: flex; justify-content: space-between; padding-top: 36px; }
  .col { width: 172px; font-size: 11px; line-height: 17px; }
  .col h3 { font-size: 15px; font-weight: 400; color: var(--white); padding-bottom: 5px;
    border-bottom: 1px solid var(--footer-line); position: relative; margin-bottom: 36px; }
  .col h3::after { content: ""; position: absolute; left: 0; bottom: -1px; width: 75px; height: 2px; background: var(--teal-bright); }
  .col p + p { margin-top: 16px; }
  .post { display: flex; gap: 10px; }
  .thumb { width: 36px; height: 34px; flex: none; }
  .post-meta { color: var(--teal-bright); line-height: 16px; }
  .post-text { margin: 8px 0 10px; padding-bottom: 10px; }
  .post-text.first { border-bottom: 1px solid var(--footer-line); }
  .contact p { margin-bottom: 6px; font-size: 10.5px; }
  .signup { display: flex; margin-top: 23px; border: 1px solid #ccc; height: 25px; }
  .signup span { flex: 1; font-size: 11px; line-height: 23px; padding-left: 9px; }
  .signup b { width: 31px; background: var(--teal); color: var(--white); font-size: 11px; text-align: center; line-height: 23px; }

  .bottombar { position: absolute; top: 1118px; left: 0; width: 1061px; height: 82px; background: var(--bottom); color: var(--footer-text); }
  .bottombar .container { display: flex; justify-content: space-between; align-items: center; height: 82px; font-size: 12px; }
  .social { display: flex; gap: 16px; margin-right: 6px; }
  .social span { width: 12px; height: 12px; border-radius: 50%; background: #6e7484; }
</style>
</head>
<body>
  <div class="topbar"><div class="container"><span>Mara Ellison welcomes you!</span><span>555-014-2287 | mara@ellisonresearch.example</span></div></div>

  <header class="header"><div class="container">
    <div class="brand"><span class="brand-dot"></span><span class="brand-name">Ellison Research Services</span></div>
    <nav class="nav"><span class="active">Home</span><span>About</span><span>Services</span><span>Contact</span><span>Publications</span><span>Blog</span><span>Links</span></nav>
  </div></header>

  <section class="hero" role="img" aria-label="Teal background with soft light bubbles">
    <div class="hero-photo" role="img" aria-label="Photo of a smiling woman in a coat and scarf holding an umbrella"></div>
    <div class="hero-text">
      <div class="hero-title">Mara Ellison</div>
      <div class="hero-sub">Professional Genealogist</div>
      <p class="hero-copy">Lorem Ipsum is simply dummy text of the printing and typesetting industry. Lorem Ipsum has been the industry's standard dummy text ever since the 1500s, when an unknown printer took a galley of type and scrambled it to make a type specimen book.</p>
    </div>
    <div class="btn">READ MORE</div>
    <div class="dots"><span class="on"></span><span></span><span></span></div>
  </section>

  <section class="welcome">
    <h1>Welcome to our Website</h1>
    <p>Lorem Ipsum is simply dummy text of the printing and typesetting industry. Lorem Ipsum has been the industry's standard dummy text ever since the 1500s, when an unknown printer took a galley of type and scrambled it to make a type specimen book. It has survived not only five centuries, but also the leap into electronic typesetting, remaining essentially unchanged.</p>
    <div class="services">
      <h2>Our Services Includes</h2>
      <ul class="service-list"><li>Forensic Genealogy</li><li>Kinship Determination</li><li>Research Analysis and Consultation</li><li>Texas Researcher</li><li>Record Retrieval</li></ul>
    </div>
  </section>

  <footer class="footer"><div class="container">
    <div class="col">
      <h3>About us</h3>
      <p>Lorem ipsum dolor sit amet, consectetur adipisicing elit, sed do eiusmod tempor incididunt. Estibulum non aliquam odio, vitae vehicula dolor.</p>
      <p>Sed congue ligula nisi, id tempor nibh tempor molestie. Duis interdum neque ligula, sit amet porttitor odio semper.</p>
    </div>
    <div class="col">
      <h3>Blog</h3>
      <div class="post"><div class="thumb" role="img" aria-label="News thumbnail" style="background:#e7a768"></div><div class="post-meta">News<br>15.3.2014</div></div>
      <p class="post-text first">Aliquam aliquam pellentesque elit vel accumsan</p>
      <div class="post"><div class="thumb" role="img" aria-label="Media thumbnail" style="background:#a3b443"></div><div class="post-meta">Media<br>9.2.2014</div></div>
      <p class="post-text">Sed venenatis, nibh et commodo malesuada nibh</p>
    </div>
    <div class="col contact">
      <h3>Contact</h3>
      <p>Ellison Research Services</p>
      <p>Mara Ellison, Professional Genealogist</p>
      <p>PO Box 4471</p>
      <p>Milford, TX 76650-4471</p>
      <p>555-014-2287</p>
    </div>
    <div class="col">
      <h3>Newsletter</h3>
      <p>Consectetur adipisicing elit, sed do eiusmod tempor incididunt ut labore aliqua.</p>
      <div class="signup"><span>email address...</span><b>Go!</b></div>
    </div>
  </div></footer>

  <div class="bottombar"><div class="container">
    <span>Copyright © 2014 Ellison Research Services | All Rights Reserved</span>
    <div class="social"><span></span><span></span><span></span><span></span><span></span></div>
  </div></div>
</body>
</html>
```